Design a New Business Card for Our Company

We are looking for fresh, unique, and a modern business card that reflects our roots as digital marketing agency focused on SEM.

Industry/Entity Type

Marketing

Contact Information for Business Card

looking for very unique out of the box designs. clean and modern that compliments our logo

Requirements
Must have
• colors should match our logo
• Front should have name, address, email, and phone/fax of the person, phone/fax are the same number
• back should have our url

```html
<!DOCTYPE html>
<html lang="en">
<head>
<meta charset="utf-8">
<title>Clearpath Media – Business Card</title>
<link href="https://fonts.googleapis.com/css2?family=Roboto:wght@300;400;500&display=swap" rel="stylesheet">
<style>
  :root {
    --backdrop: #b1afb0;
    --card: #ffffff;
    --brand-blue: #5b97d5;
    --brand-grey: #8f8f8f;
    --ink: #222222;
    --pattern: #f3f3f3;
  }
  * { margin: 0; padding: 0; box-sizing: border-box; }
  html, body { width: 1200px; height: 1000px; overflow: hidden; }
  body {
    background: var(--backdrop);
    font-family: "Roboto", Arial, sans-serif;
    position: relative;
  }
  .card {
    position: absolute;
    width: 703px;
    height: 430px;
    background: var(--card);
    box-shadow: 6px 8px 12px rgba(0,0,0,0.35);
  }
  .card--back { left: 248px; top: 48px; }
  .card--front { left: 250px; top: 522px; }

  .pattern-band {
    position: absolute;
    left: 8px;
    right: 8px;
  }
  .pattern-band--top {
    top: 6px; height: 150px;
    background: linear-gradient(to bottom, var(--pattern) 0%, var(--pattern) 55%, rgba(243,243,243,0) 100%);
  }
  .pattern-band--bottom {
    top: 276px; height: 150px;
    background: linear-gradient(to bottom, rgba(243,243,243,0) 0%, var(--pattern) 40%, var(--pattern) 100%);
  }

  .brand {
    position: absolute;
    left: 0; right: 0;
    display: flex;
    align-items: center;
    justify-content: center;
    gap: 14px;
  }
  .brand__dot {
    width: 30px; height: 30px;
    border-radius: 50%;
    background: var(--brand-blue);
  }
  .brand__name {
    font-size: 44px;
    font-weight: 500;
    color: var(--brand-blue);
    letter-spacing: -0.5px;
  }
  .card--back .brand { top: 182px; }
  .card--front .brand { top: 83px; }

  .website {
    position: absolute;
    left: 0; right: 0;
    top: 381px;
    text-align: center;
    font-size: 21px;
    font-weight: 500;
    color: var(--brand-blue);
  }

  .person {
    position: absolute;
    left: 8px; right: 6px;
    top: 221px;
    display: flex;
    align-items: center;
    gap: 8px;
  }
  .person__rule { flex: 1; height: 3px; background: var(--brand-blue); }
  .person__name { font-size: 25px; font-weight: 500; color: var(--brand-blue); }
  .person__title {
    position: absolute;
    left: 0; right: 0;
    top: 247px;
    text-align: center;
    font-size: 20px;
    font-weight: 300;
    color: var(--brand-grey);
  }

  .contacts {
    position: absolute;
    top: 286px;
    left: 0; right: 0;
  }
  .contact {
    position: absolute;
    width: 180px;
    margin-left: -90px;
    text-align: center;
    font-size: 16px;
    font-weight: 300;
    line-height: 20px;
    color: var(--ink);
  }
  .contact svg { display: block; margin: 0 auto; width: 28px; height: 28px; }
  .contact__text { margin-top: 13px; }
  .contact__text--single { margin-top: 33px; }
  .contact--address { left: 101px; }
  .contact--phone { left: 265px; }
  .contact--fax { left: 432px; }
  .contact--email { left: 596px; }
</style>
</head>
<body>

<section class="card card--back">
  <div class="pattern-band pattern-band--top" role="img" aria-label="Faint repeating brand pattern"></div>
  <div class="pattern-band pattern-band--bottom" role="img" aria-label="Faint repeating brand pattern"></div>
  <div class="brand">
    <span class="brand__dot"></span>
    <span class="brand__name">Clearpath Media</span>
  </div>
  <p class="website">www.clearpathmedia.com</p>
</section>

<section class="card card--front">
  <div class="brand">
    <span class="brand__dot"></span>
    <span class="brand__name">Clearpath Media</span>
  </div>

  <div class="person">
    <span class="person__rule"></span>
    <span class="person__name">John Doe</span>
    <span class="person__rule"></span>
  </div>
  <p class="person__title">President</p>

  <div class="contacts">
    <div class="contact contact--address">
      <svg viewBox="0 0 28 28" aria-hidden="true">
        <circle cx="14" cy="14" r="12.5" fill="none" stroke="#5b97d5" stroke-width="2"/>
        <path d="M14 7a4.5 4.5 0 0 0-4.5 4.5c0 3.4 4.5 9 4.5 9s4.5-5.6 4.5-9A4.5 4.5 0 0 0 14 7z" fill="none" stroke="#5b97d5" stroke-width="1.8"/>
        <circle cx="14" cy="11.5" r="1.6" fill="#5b97d5"/>
      </svg>
      <p class="contact__text">1450 Larkspur Ave<br>Sun Valley,<br>CA 91352 USA</p>
    </div>
    <div class="contact contact--phone">
      <svg viewBox="0 0 28 28" aria-hidden="true">
        <circle cx="14" cy="14" r="12.5" fill="none" stroke="#5b97d5" stroke-width="2"/>
        <path d="M9.5 8.5l2.3-.8 1.6 3.1-1.4 1.2c.7 1.6 2 2.9 3.6 3.7l1.2-1.4 3.1 1.6-.8 2.3c-5 .3-9.9-4.6-9.6-9.7z" fill="#5b97d5"/>
      </svg>
      <p class="contact__text contact__text--single">888-555-0147</p>
    </div>
    <div class="contact contact--fax">
      <svg viewBox="0 0 28 28" aria-hidden="true">
        <circle cx="14" cy="14" r="12.5" fill="none" stroke="#5b97d5" stroke-width="2"/>
        <rect x="10" y="7.5" width="8" height="4" fill="#5b97d5"/>
        <rect x="8" y="11.5" width="12" height="6" rx="1" fill="#5b97d5"/>
        <rect x="10" y="16" width="8" height="4.5" fill="#fff" stroke="#5b97d5" stroke-width="1.4"/>
      </svg>
      <p class="contact__text contact__text--single">888-555-0147</p>
    </div>
    <div class="contact contact--email">
      <svg viewBox="0 0 28 28" aria-hidden="true">
        <circle cx="14" cy="14" r="12.5" fill="none" stroke="#5b97d5" stroke-width="2"/>
        <rect x="8" y="9.5" width="12" height="9" fill="#5b97d5"/>
        <path d="M8 9.8l6 4.8 6-4.8" fill="none" stroke="#fff" stroke-width="1.3"/>
      </svg>
      <p class="contact__text contact__text--single">hi@clearpath.com</p>
    </div>
  </div>
</section>

</body>
</html>
```